Need a business card for our overland brand!

We had the logo made and we need a great design for our business card. Use the logo provide or tweak it however you see fit.

Contact Information for Business Card

Name, Title, Telephone, email, website

```html
<!DOCTYPE html>
<html lang="en">
<head>
<meta charset="utf-8">
<title>Northpass Expeditions — Business Card</title>
<link rel="stylesheet" href="https://fonts.googleapis.com/css2?family=Montserrat:wght@400;500;700&display=swap">
<style>
  :root {
    --page: #dcdfdd;
    --card: #f1f1f1;
    --navy: #22354f;
    --blue: #1a93b3;
    --ink: #22354f;
    --light-ink: #eef2f6;
  }
  html, body {
    margin: 0;
    padding: 0;
    width: 1200px;
    height: 1200px;
    overflow: hidden;
    background: var(--page);
  }
  .canvas {
    position: relative;
    width: 1200px;
    height: 1200px;
  }
  .card {
    position: absolute;
    left: 150px;
    width: 900px;
    height: 514px;
    border-radius: 6px;
    overflow: hidden;
    background: var(--card);
    box-shadow: 0 10px 28px rgba(0,0,0,0.18);
  }
  .card--front { top: 60px; }
  .card--back  { top: 626px; }
  .card svg { display: block; width: 100%; height: 100%; }
  .holder-name {
    font-family: "Montserrat", sans-serif;
    font-weight: 700;
    font-size: 46px;
    fill: var(--blue);
  }
  .holder-title {
    font-family: "Montserrat", sans-serif;
    font-weight: 500;
    font-size: 29px;
    fill: var(--ink);
  }
  .contact-line {
    font-family: "Montserrat", sans-serif;
    font-weight: 400;
    font-size: 28px;
    fill: var(--light-ink);
  }
  .brand-name {
    font-family: "Montserrat", sans-serif;
    font-weight: 700;
    fill: var(--navy);
  }
  .brand-dot { fill: var(--blue); }
  .band-navy { fill: var(--navy); }
  .band-blue { fill: var(--blue); }
  .contact-icon { fill: none; stroke: var(--light-ink); stroke-width: 2.4; stroke-linecap: round; stroke-linejoin: round; }
</style>
</head>
<body>
<div class="canvas">

  <section class="card card--front">
    <svg viewBox="0 0 1173 670" xmlns="http://www.w3.org/2000/svg">
      <path class="band-blue" d="M0,272 C420,250 820,390 1173,438 L1173,456 C820,408 420,268 0,290 Z"/>
      <path class="band-navy" d="M0,304 C420,282 820,422 1173,470 L1173,670 L0,670 Z"/>

      <text class="holder-name" x="87" y="118">Rowan Hale</text>
      <text class="holder-title" x="87" y="166">Founder &amp; Director</text>

      <circle class="brand-dot" cx="620" cy="120" r="12"/>
      <text class="brand-name" x="1090" y="133" font-size="36" text-anchor="end">Northpass Expeditions</text>

      <text class="contact-line" x="87" y="390">418 Cedar Hollow Lane</text>
      <text class="contact-line" x="87" y="430">Pine Ridge Oregon 97321</text>

      <g class="contact-icon">
        <path d="M92,490 c-3,4 0,12 6,17 c6,6 13,9 17,6 l2,-3 l-5,-5 l-3,2 c-3,-1 -8,-6 -9,-9 l2,-3 l-5,-5 Z"/>
        <rect x="87" y="534" width="24" height="16" rx="1"/>
        <path d="M87,535 l12,9 l12,-9"/>
        <circle cx="99" cy="586" r="11"/>
        <path d="M88,586 h22 M99,575 c-6,6 -6,16 0,22 c6,-6 6,-16 0,-22"/>
      </g>
      <text class="contact-line" x="127" y="508">(555)-214-3370</text>
      <text class="contact-line" x="127" y="552">hello@northpassexpeditions.com</text>
      <text class="contact-line" x="127" y="596">www.northpassexpeditions.com</text>
    </svg>
  </section>

  <section class="card card--back">
    <svg viewBox="0 0 1173 670" xmlns="http://www.w3.org/2000/svg">
      <circle class="brand-dot" cx="586" cy="250" r="22"/>
      <text class="brand-name" x="586" y="380" font-size="60" text-anchor="middle">Northpass Expeditions</text>
    </svg>
  </section>

</div>
</body>
</html>
```